Hollow Bluff Cellars Reserve Cabernet Sauvignon Wine Labels front and back

I need a front and back wine label. For a new RESERVE Cabernet Sauvignon wine. I am attaching the details and some ideas and possible images to use. But creativity is encouraged. This wine will be seen on wine shop and grocery store shelves so it needs to pop while appearing elegant and to be about $50/bottle of wine. The front and back labels should go together nicely. I would like some foil on the front, but not the back. We are trying to show the natural beauty of our vineyards and the elegance of our wines. We would like to invoke a feel of sustainability, proudly family owned and operated.

Target Market(s)

21-50 year olds, red wine drinkers, higher priced wine drinkers

Industry/Entity Type

Wine

Font styles to use
Serif
Script

Colors

Designer to choose only greyscale colors for use in the design.

Requirements
Must have
• Front Label with specified details and Back label with specified details. Foil banner on the front label that says " Family stewards of the land for 5 generations"the front label that says
Nice to have
• vineyard or winery background, have include a sample or example, some gold or bronze or silver accents

```html
<!DOCTYPE html>
<html lang="en">
<head>
<meta charset="utf-8">
<title>Hollow Bluff Cellars Reserve Cabernet Sauvignon Labels</title>
<link rel="stylesheet" href="https://fonts.googleapis.com/css2?family=Cinzel:wght@400;700&family=Cormorant+SC:wght@500;600&family=EB+Garamond:wght@400&family=Pinyon+Script&display=swap">
<style>
  :root {
    --page: #ffffff;
    --label: #100d0b;
    --silver: #c4c4c4;
    --silver-soft: #d6d6d6;
    --text-light: #d2d2d2;
    --gold-pale: #f6e7a4;
    --gold: #c9a24a;
    --gold-deep: #8a5a1c;
    --gold-bright: #d5a32a;
    --band-ink: #2a1b08;
  }
  * { margin: 0; padding: 0; box-sizing: border-box; }
  html, body { width: 1200px; height: 1200px; overflow: hidden; background: var(--page); }
  .canvas { position: relative; width: 1200px; height: 1200px; }

  .label { position: absolute; background: var(--label); border-radius: 9px; overflow: hidden; }

  /* Front label */
  .front { left: 85px; top: 212px; width: 508px; height: 777px; }
  .brand-rule { position: absolute; top: 70px; left: 0; width: 100%; height: 5px; }
  .brand-rule span { position: absolute; top: 0; height: 1px; background: linear-gradient(90deg, var(--gold-deep), var(--gold), var(--gold-pale)); }
  .brand-rule .l { left: 0; width: 175px; }
  .brand-rule .l + .l { top: 4px; }
  .brand-rule .r { right: 0; width: 175px; background: linear-gradient(90deg, var(--gold-pale), var(--gold), var(--gold-deep)); }
  .brand-rule .r + .r { top: 4px; }
  .brand-mark {
    position: absolute; top: 40px; left: 50%; transform: translateX(-50%);
    width: 70px; height: 70px; border: 2px solid var(--gold);
    display: flex; align-items: center; justify-content: center; text-align: center;
    font-family: "Cinzel", serif; font-weight: 400; font-size: 10px; line-height: 13px;
    color: var(--gold); letter-spacing: 0.5px;
  }
  .winery-name {
    position: absolute; top: 150px; width: 100%; text-align: center;
    font-family: "Cinzel", serif; font-weight: 400; font-size: 45px; line-height: 47px;
    color: var(--silver); letter-spacing: 1px;
  }
  .tier {
    position: absolute; top: 318px; width: 100%; text-align: center;
    font-family: "Pinyon Script", cursive; font-size: 86px; line-height: 100px;
    background: linear-gradient(90deg, var(--gold-pale), var(--gold) 45%, var(--gold-deep) 80%, var(--gold-bright));
    -webkit-background-clip: text; background-clip: text; color: transparent;
  }
  .tier-flourish {
    position: absolute; top: 410px; left: 146px; width: 216px; height: 40px;
    background: radial-gradient(ellipse at center, rgba(201,162,74,0.45), rgba(201,162,74,0) 70%);
  }
  .region {
    position: absolute; top: 465px; width: 100%; text-align: center;
    font-family: "Cormorant SC", serif; font-weight: 500; font-size: 24px; letter-spacing: 2.5px;
    color: var(--text-light);
  }
  .divider { position: absolute; top: 530px; left: 173px; width: 161px; height: 10px; }
  .varietal {
    position: absolute; top: 576px; width: 100%; text-align: center;
    font-family: "Cormorant SC", serif; font-weight: 600; font-size: 22px; letter-spacing: 2.5px;
    color: var(--silver-soft);
  }
  .vintage {
    position: absolute; top: 597px; width: 100%; text-align: center;
    font-family: "EB Garamond", serif; font-size: 19px; letter-spacing: 1.5px; color: var(--silver);
  }
  .heritage-band {
    position: absolute; left: 0; bottom: 0; width: 100%; height: 55px;
    background: linear-gradient(90deg, var(--gold-pale) 0%, #d8c27a 25%, var(--gold-deep) 55%, #b98224 72%, var(--gold-bright) 100%);
    display: flex; align-items: center; justify-content: center;
    font-family: "Cinzel", serif; font-weight: 700; font-size: 14.5px; letter-spacing: 1.8px;
    color: var(--band-ink);
  }

  /* Back label */
  .back { left: 650px; top: 330px; width: 465px; height: 544px; }
  .back-title {
    position: absolute; top: 44px; width: 100%; text-align: center;
    font-family: "Cinzel", serif; font-weight: 400; font-size: 28px; letter-spacing: 0.5px;
    color: var(--silver);
  }
  .story {
    position: absolute; top: 79px; left: 45px; width: 375px; text-align: center;
    font-family: "EB Garamond", serif; font-size: 14.2px; line-height: 19.8px; color: var(--text-light);
  }
  .signature {
    position: absolute; top: 192px; left: 95px; width: 275px; height: 50px;
    background: radial-gradient(ellipse at center, rgba(213,163,42,0.4), rgba(213,163,42,0) 70%);
  }
  .signoff {
    position: absolute; top: 246px; width: 100%; text-align: center;
    font-family: "EB Garamond", serif; font-size: 14.5px; line-height: 16.6px; color: var(--text-light);
  }
  .warning {
    position: absolute; top: 372px; left: 17px; width: 245px;
    font-family: "EB Garamond", serif; font-size: 12.4px; line-height: 19.8px; color: var(--text-light);
  }
  .column-rule { position: absolute; left: 266px; top: 352px; width: 1px; height: 150px; background: #8a8a8a; }
  .specs {
    position: absolute; top: 350px; left: 276px; width: 180px;
    font-family: "EB Garamond", serif; font-size: 13.5px; line-height: 17px; color: var(--text-light);
  }
  .specs .producer { margin-top: 3px; font-size: 8.6px; line-height: 11px; }
</style>
</head>
<body>
<main class="canvas">

  <section class="label front" aria-label="Front label">
    <div class="brand-rule">
      <span class="l"></span><span class="l"></span>
      <span class="r"></span><span class="r"></span>
    </div>
    <div class="brand-mark">Hollow<br>Bluff<br>Cellars</div>

    <h1 class="winery-name">HOLLOW BLUFF<br>CELLARS</h1>

    <div class="tier">Reserve</div>
    <div class="tier-flourish" role="img" aria-label="Gold scroll flourish beneath the Reserve lettering"></div>

    <p class="region">Horse Heaven Hills</p>

    <svg class="divider" viewBox="0 0 161 10" aria-hidden="true">
      <defs>
        <linearGradient id="divGold" x1="0" x2="1">
          <stop offset="0" stop-color="#f6e7a4"/><stop offset="0.5" stop-color="#c9a24a"/><stop offset="1" stop-color="#d5a32a"/>
        </linearGradient>
      </defs>
      <line x1="0" y1="5" x2="161" y2="5" stroke="url(#divGold)" stroke-width="1"/>
      <path d="M0 5 L12 2.5 L20 5 L12 7.5 Z" fill="url(#divGold)"/>
      <path d="M161 5 L149 2.5 L141 5 L149 7.5 Z" fill="url(#divGold)"/>
      <circle cx="29" cy="5" r="2" fill="#c9a24a"/>
      <circle cx="132" cy="5" r="2" fill="#c9a24a"/>
    </svg>

    <p class="varietal">Cabernet Sauvignon</p>
    <p class="vintage">2022</p>

    <div class="heritage-band">FAMILY STEWARDS OF THE LAND FOR 5 GENERATIONS</div>
  </section>

  <section class="label back" aria-label="Back label">
    <h2 class="back-title">HOLLOW BLUFF CELLARS</h2>
    <p class="story">″Our vineyards, nestled along the Columbia River in Washington state, flourish in a region celebrated for its long, hot days and cool, crisp nights. This area, rich in natural resources and fertile soils, imparts a unique essence of balance, structure, and elegance to our wines.″</p>

    <div class="signature" role="img" aria-label="Winemaker's handwritten gold signature"></div>
    <p class="signoff">Cheers<br>Maren Holloway<br>Winemaker</p>

    <p class="warning">GOVERNMENT WARNING:<br>(1) According to the Surgeon General, women should not drink alcoholic beverages during pregnancy because of the risk of birth defects. (2) Consumption of alcoholic beverages impairs your ability to drive a car or operate machinery, and may cause health problems.</p>
    <div class="column-rule"></div>
    <div class="specs">
      750 ML<br>CONTAINS SULFITES<br>15% ALC. BY VOL.
      <p class="producer">PRODUCED AND BOTTLED BY RIDGELINE<br>WINE ESTATES, LLC, BENTON WA, USA</p>
    </div>
  </section>

</main>
</body>
</html>
```